Home page web design for a lawn specialist business

-The design must be based around the attached HPID (home page information design) called Turf Tidings HPID. I've attached Word and PDF versions - these are the same. The table boxes are just for approximate placement of information and you can use boxes and bold shapes for this design.

All fonts used in the HPID are only examples - you can use any Google font you wish.

- Text that is in orange is for your information only. Text to go on the design is black. Some instructions are in the HPID. Please be creative!

-The design needs to be modern and exciting - colours are to be the green of the logo, and white ...and then choose dark green, or dark grey or black.

Logo - attached (it's not great quality but don't worry, we'll replace it later)

- I've provided the images for the galleries - they are labelled and will match the name in the HPID. Please use the supplied images!

- Examples of some websites that have great design... don't copy them please but they are similar in look to what we are after....
www.qmbbuildworks.co.nz
http://www.rim-safeguard.co.nz/
http://www.lumenhomes.wb.gs/

Important: Width of content will be 1280 pixels when implemented as a web page but the winning design will need to supplied be on a 2000 pixel wide background so nav bars and background can extend outside the 1280 width.
Header height (without nav bar) 150-160 pixels.

We don't comment on individual designs but will choose a winning design promptly.

Industry/Entity Type

Business

Number of Pages Required

1 page

Font styles to use
Sans Serif

Requirements
Must have
• clean, modern, well-spaced design

```html
<!DOCTYPE html>
<html lang="en">
<head>
<meta charset="utf-8">
<title>Turf Tidings – Lawn specialists</title>
<link href="https://fonts.googleapis.com/css2?family=Open+Sans:ital,wght@0,400;0,600;0,700;0,800;1,700&display=swap" rel="stylesheet">
<style>
  :root {
    --green: #3f9a1c;
    --green-dark: #2d7a12;
    --green-light: #8cc63f;
    --nav-bg: #1c1c1c;
    --nav-border: #333;
    --text: #2b2b2b;
    --text-soft: #444;
    --bg: #ffffff;
    --panel: #f2f2f2;
  }
  * { margin: 0; padding: 0; box-sizing: border-box; }
  html, body { width: 1200px; height: 1000px; overflow: hidden; }
  body { background: var(--bg); font-family: "Open Sans", Arial, sans-serif; color: var(--text); position: relative; }

  .site-header { position: absolute; top: 0; left: 0; width: 1200px; height: 98px; }
  .brand { position: absolute; left: 208px; top: 22px; display: flex; align-items: center; gap: 10px; }
  .brand-mark { width: 26px; height: 26px; background: var(--green); }
  .brand-name { font-size: 26px; font-weight: 800; color: var(--green); letter-spacing: -0.5px; }
  .header-info { position: absolute; left: 600px; width: 455px; top: 10px; text-align: center; }
  .header-title { font-size: 17px; font-weight: 600; color: #333; }
  .header-sub { font-size: 11px; color: #444; margin-top: 6px; }
  .header-phone { font-size: 23px; font-weight: 700; color: var(--green); margin-top: 6px; letter-spacing: 0.5px; }
  .grass-edge { position: absolute; left: 0; top: 80px; width: 1200px; height: 18px;
    background: linear-gradient(to bottom, rgba(140,198,63,0) 0%, var(--green-light) 55%, var(--green) 100%); }

  .main-nav { position: absolute; top: 98px; left: 0; width: 1200px; height: 35px; background: var(--nav-bg); }
  .main-nav ul { list-style: none; display: flex; position: absolute; left: 208px; top: 0; height: 35px; border-left: 1px solid var(--nav-border); }
  .main-nav li { height: 35px; padding: 0 15px; display: flex; align-items: center; border-right: 1px solid var(--nav-border);
    font-size: 9px; font-weight: 700; color: #fff; text-transform: uppercase; letter-spacing: 0.2px; }
  .main-nav li.active { background: var(--green-dark); }

  .intro-panel { position: absolute; top: 133px; left: 150px; width: 900px; height: 627px;
    background: radial-gradient(ellipse at center, #ececec 0%, #f5f5f5 60%, rgba(255,255,255,0) 100%); }

  .hero-slider { position: absolute; left: 207px; top: 150px; width: 786px; height: 317px; background: #fff; padding: 3px;
    box-shadow: 0 4px 10px rgba(0,0,0,0.15); }
  .hero-slide { display: flex; width: 100%; height: 100%; position: relative; }
  .slide-before { flex: 1; background: linear-gradient(135deg, #d9d3c9 0%, #6e5a4a 40%, #5d4a3c 100%); }
  .slide-after { flex: 1; background: linear-gradient(135deg, #e9e4dc 0%, #4a9a2a 40%, #3b8a1f 100%); }
  .slide-label { position: absolute; bottom: 18px; font-size: 16px; font-weight: 700; font-style: italic; color: #fff; }
  .slide-label.before { left: 300px; }
  .slide-label.after { right: 24px; }
  .slider-arrow { position: absolute; top: 296px; width: 36px; height: 36px; border-radius: 50%; background: #fff;
    box-shadow: 0 1px 4px rgba(0,0,0,0.2); display: flex; align-items: center; justify-content: center; }
  .slider-arrow.prev { left: 191px; }
  .slider-arrow.next { left: 974px; }

  .intro { position: absolute; left: 207px; width: 786px; top: 490px; text-align: center; }
  .intro h1 { font-size: 19px; font-weight: 600; color: #333; }
  .intro h1 strong { font-weight: 700; color: #111; }
  .intro .tagline { font-size: 14px; color: #444; margin-top: 6px; }
  .intro-copy { position: absolute; left: 207px; width: 786px; top: 585px; text-align: center; font-size: 11.5px; line-height: 22px; color: var(--text-soft); }
  .intro-copy p + p { margin-top: 18px; }
  .intro-emblem { position: absolute; left: 520px; top: 555px; width: 160px; height: 190px; border-radius: 50%;
    background: radial-gradient(circle, rgba(0,0,0,0.06) 0%, rgba(0,0,0,0) 70%); }

  .service-card { position: absolute; top: 783px; width: 380px; }
  .service-card.seeding { left: 207px; }
  .service-card.care { left: 613px; }
  .service-image { width: 380px; height: 180px; }
  .seeding .service-image { background: linear-gradient(to bottom, #8a8a7a 0%, #6b7a50 40%, #3f8f93 65%, #2f7f84 100%); }
  .care .service-image { background: radial-gradient(circle at 40% 70%, #5fb32d 0%, #2e7a14 70%, #1f5c0c 100%); }
  .service-title { text-align: center; font-size: 13px; font-weight: 600; color: #111; margin-top: 15px; }
</style>
</head>
<body>
  <header class="site-header">
    <div class="brand"><span class="brand-mark"></span><span class="brand-name">Turf Tidings</span></div>
    <div class="header-info">
      <div class="header-title">Lawn specialists</div>
      <div class="header-sub">From ground preparation to lawn aftercare servicing the Auckland region</div>
      <div class="header-phone">0800 24 68 10</div>
    </div>
    <div class="grass-edge" role="img" aria-label="Grass blades edging the header"></div>
  </header>

  <nav class="main-nav">
    <ul>
      <li class="active">Home</li>
      <li>About us</li>
      <li>Services</li>
      <li>Lawn care</li>
      <li>Seasonal care</li>
      <li>Hydroseeding</li>
      <li>FAQs</li>
      <li>Before &amp; after gallery</li>
      <li>Quote/contact</li>
    </ul>
  </nav>

  <div class="intro-panel"></div>

  <section class="hero-slider">
    <div class="hero-slide">
      <div class="slide-before" role="img" aria-label="Courtyard with bare prepared soil before seeding"></div>
      <div class="slide-after" role="img" aria-label="Same courtyard with a lush green lawn after seeding"></div>
      <span class="slide-label before">Before</span>
      <span class="slide-label after">After</span>
    </div>
  </section>
  <div class="slider-arrow prev"><svg width="10" height="10" viewBox="0 0 10 10"><path d="M6.5 1.5 3 5l3.5 3.5" fill="none" stroke="#333" stroke-width="1.8"/></svg></div>
  <div class="slider-arrow next"><svg width="10" height="10" viewBox="0 0 10 10"><path d="M3.5 1.5 7 5 3.5 8.5" fill="none" stroke="#333" stroke-width="1.8"/></svg></div>

  <section class="intro">
    <h1>You can always spot an <strong>Turf Tidings lawn</strong></h1>
    <p class="tagline">It’s the one that turns your neighbours green with envy</p>
  </section>
  <div class="intro-emblem" role="img" aria-label="Faint horticulture diploma emblem"></div>
  <div class="intro-copy">
    <p>If you want a lawn or playing field that looks good throughout the year, talk to us. Turf Tidings are New Zealand’s experts in high quality grass seeding and lawn maintenance, creating the lushest lawns you’ll ever see. With high-tech equipment, years of experience and expert aftercare, nobody knows grass like Turf Tidings.</p>
    <p>There are many factors that influence the quality of a lawn, including seasonality, growing conditions, shade, seed types, and time. A one-size-fits-all solution couldn’t possibly guarantee a great lawn, so we provide personalised advice, a full range of seeding techniques.</p>
  </div>

  <article class="service-card seeding">
    <div class="service-image" role="img" aria-label="Freshly hydroseeded garden bed in blue-green mulch"></div>
    <h2 class="service-title">Grass seeding services</h2>
  </article>
  <article class="service-card care">
    <div class="service-image" role="img" aria-label="Sprinkler watering a green lawn"></div>
    <h2 class="service-title">Lawn care maintenance</h2>
  </article>
</body>
</html>
```